Business Card design for a company called Tully Brook Co

I need a business card design for my oil fired boiler servicing company. I have a logo design already and Im just looking that incorporated into the business card design. card details; Tully Brook Co
Oil Burner Servicing - Mid Ulster Area
Service Engineer - Owen Madler
Mobile 07700914862
email - Tully.Brook.Co@quillpost.net
www.tullybrookco.net
I carry out Servicing, Commissioning, Fault Finding, Warranty Validation
Target Market(s)
home owners with oil fired central heating
Industry/Entity Type
Business
Contact Information for Business Card
Tully Brook Co
Tell. 07700914862
Web: www.tullybrookco.net
email Tully.Brook.Co@Quillpost.Net
Servicing Fault Finding Commissioning Warranty Validation
Look and feel

```html
<!DOCTYPE html>
<html lang="en">
<head>
<meta charset="utf-8">
<title>Tully Brook Co – Business Card</title>
<link rel="stylesheet" href="https://fonts.googleapis.com/css2?family=Nunito:wght@700&family=Arimo:wght@400;700&display=swap">
<style>
  :root {
    --page: #e9e7e3;
    --card-white: #f7f7f7;
    --card-black: #141414;
    --brand-green: #5cbf2f;
    --brand-green-light: #8fd94a;
    --text-white: #ffffff;
    --text-soft: #e4e4e4;
    --divider: #bdbdbd;
  }
  * { margin: 0; padding: 0; box-sizing: border-box; }
  html, body { width: 1200px; height: 902px; overflow: hidden; }
  body {
    background: var(--page);
    position: relative;
    font-family: "Arimo", Arial, sans-serif;
  }
  .business-card {
    position: absolute;
    left: 150px;
    top: 194px;
    width: 900px;
    height: 514px;
    background: var(--card-white);
    box-shadow: 0 10px 30px rgba(0,0,0,0.25);
    overflow: hidden;
  }
  .card-shapes { position: absolute; inset: 0; }
  .brand {
    position: absolute;
    left: 80px;
    top: 78px;
    display: flex;
    align-items: center;
    gap: 26px;
  }
  .brand-dot {
    width: 120px;
    height: 120px;
    border-radius: 50%;
    background: var(--brand-green);
    flex: none;
  }
  .brand-name {
    font-family: "Nunito", Arial, sans-serif;
    font-weight: 700;
    font-size: 78px;
    line-height: 1;
    color: var(--brand-green);
    letter-spacing: -1px;
  }
  .brand-tagline {
    position: absolute;
    left: 226px;
    top: 172px;
    font-family: "Nunito", Arial, sans-serif;
    font-weight: 700;
    font-size: 17px;
    letter-spacing: 2.6px;
    color: var(--brand-green);
    text-transform: uppercase;
  }
  .engineer {
    position: absolute;
    left: 60px;
    top: 360px;
    color: var(--text-white);
  }
  .engineer-name { font-size: 40px; font-weight: 700; line-height: 1.05; }
  .engineer-role { font-size: 29px; color: var(--text-soft); margin-top: 4px; }
  .services {
    position: absolute;
    left: 60px;
    top: 466px;
    font-size: 23px;
    color: var(--text-white);
    word-spacing: 2px;
  }
  .services strong { font-weight: 700; }
  .contact-divider {
    position: absolute;
    left: 540px;
    top: 300px;
    width: 1.5px;
    height: 130px;
    background: var(--divider);
  }
  .contact-list {
    position: absolute;
    left: 560px;
    top: 290px;
    list-style: none;
    color: var(--text-white);
    font-size: 22px;
  }
  .contact-list li {
    display: flex;
    align-items: center;
    gap: 16px;
    height: 42px;
  }
  .contact-icon { width: 22px; height: 22px; flex: none; }
</style>
</head>
<body>
  <article class="business-card">
    <svg class="card-shapes" width="900" height="514" viewBox="0 0 900 514" aria-hidden="true">
      <defs>
        <linearGradient id="greenLine" x1="0" x2="1" y1="0" y2="0">
          <stop offset="0" stop-color="#5cbf2f"/>
          <stop offset="1" stop-color="#8fd94a"/>
        </linearGradient>
      </defs>
      <polygon points="0,262 0,514 900,514 900,196 876,196 836,280 66,280 44,262" fill="#141414"/>
      <polyline points="70,268 828,268 866,190" fill="none" stroke="url(#greenLine)" stroke-width="7" stroke-linejoin="miter"/>
    </svg>

    <div class="brand">
      <span class="brand-dot"></span>
      <span class="brand-name">Tully Brook Co</span>
    </div>
    <p class="brand-tagline">Oil Burner Servicing - Mid Ulster Area</p>

    <div class="engineer">
      <p class="engineer-name">Owen Madler</p>
      <p class="engineer-role">Service Engineer</p>
    </div>

    <span class="contact-divider"></span>
    <ul class="contact-list">
      <li>
        <svg class="contact-icon" viewBox="0 0 22 22" aria-hidden="true">
          <rect x="1" y="1" width="20" height="20" rx="2" fill="#fff"/>
          <path d="M7 5c1 0 2 2 2 3s-1 1-1 2 2 4 4 4 1-1 2-1 3 1 3 2-1 2-3 2C9 17 5 13 5 8c0-2 1-3 2-3z" fill="#141414"/>
        </svg>
        <span>07700914862</span>
      </li>
      <li>
        <svg class="contact-icon" viewBox="0 0 22 22" aria-hidden="true">
          <rect x="1" y="1" width="20" height="20" rx="2" fill="#fff"/>
          <circle cx="11" cy="11" r="6.5" fill="none" stroke="#141414" stroke-width="1.6"/>
          <ellipse cx="11" cy="11" rx="2.8" ry="6.5" fill="none" stroke="#141414" stroke-width="1.3"/>
          <line x1="4.5" y1="11" x2="17.5" y2="11" stroke="#141414" stroke-width="1.3"/>
        </svg>
        <span>www.tullybrookco.net</span>
      </li>
      <li>
        <svg class="contact-icon" viewBox="0 0 22 22" aria-hidden="true">
          <rect x="1" y="1" width="20" height="20" rx="2" fill="#fff"/>
          <rect x="4" y="6" width="14" height="10" fill="none" stroke="#141414" stroke-width="1.6"/>
          <polyline points="4,6 11,12 18,6" fill="none" stroke="#141414" stroke-width="1.6"/>
        </svg>
        <span>Tully.Brook.Co@Quillpost.Net</span>
      </li>
    </ul>

    <p class="services">Servicing Fault Finding Commissioning <strong>Warranty Validation</strong></p>
  </article>
</body>
</html>
```